SkyvoraQ Business Cards and Stationary Design

Need a design for our business cards and stationary. I want to carry on the theme of the logo. I want the business cards to have a design on the back. I would like the business cards and the stationary to carry the same theme, design scheme, and branding

Target Market(s)

Airlines and Maintenance Facilities

Industry/Entity Type

Aviation

Contact Information for Business Card

Name
Position Title
Address: 4827 Tollbeck Lane, Fort Pierce, Florida, 34951
Office Number
Mobile Number
Email
Website

Font styles to use
Serif
Sans Serif

Colors

Designer to choose colors to be used in the design.

```html
<!DOCTYPE html>
<html lang="en">
<head>
<meta charset="utf-8">
<title>SkyvoraQ Business Card</title>
<link href="https://fonts.googleapis.com/css2?family=Arimo:wght@400;700&display=swap" rel="stylesheet">
<style>
  :root {
    --card-navy: #0a2f52;
    --brand-blue: #1d4284;
    --text-white: #ffffff;
  }
  html, body {
    margin: 0;
    padding: 0;
    width: 1200px;
    height: 720px;
    overflow: hidden;
    background: var(--card-navy);
  }
  .business-card {
    position: relative;
    width: 1200px;
    height: 720px;
    overflow: hidden;
    background: var(--card-navy);
    font-family: "Arimo", Helvetica, Arial, sans-serif;
    color: var(--text-white);
  }
  .brand-name {
    position: absolute;
    left: 48px;
    top: 300px;
    margin: 0;
    font-size: 92px;
    font-weight: 700;
    letter-spacing: -1px;
    color: var(--brand-blue);
    line-height: 1;
  }
  .contact-block {
    position: absolute;
    left: 671px;
    top: 106px;
    font-size: 32px;
    line-height: 42.7px;
    font-weight: 400;
  }
  .contact-block p {
    margin: 0;
    white-space: nowrap;
  }
  .contact-details {
    font-style: normal;
  }
  .contact-name {
    font-weight: 700;
  }
  .group-gap {
    margin-top: 42.7px !important;
  }
  .label {
    display: inline-block;
    min-width: 42px;
  }
</style>
</head>
<body>
  <main class="business-card">
    <p class="brand-name">SkyvoraQ</p>

    <section class="contact-block">
      <p class="contact-name">Marlon Teague</p>
      <p class="contact-title">President</p>

      <address class="contact-details">
        <p class="group-gap">4827 Tollbeck Lane</p>
        <p>Fort Pierce</p>
        <p>Florida, 34951</p>

        <p class="group-gap"><span class="label">P:</span>772.555.0148</p>
        <p><span class="label">M:</span>772.555.0193</p>
        <p><span class="label">E:</span>marlon@skyvoraq.com</p>
        <p>www.skyvoraq.com</p>
      </address>
    </section>
  </main>
</body>
</html>
```